Website Performance Testing eBook for the software testing industry

Overview:
I would like an ebook/whitepaper designed. This ebook will be digital published on my website as a lead generation piece. The purpose is to give high level tips on what to look for and things to think about when working on a website performance testing project.
The ebook also demonstrates our expertise and knowledge on the topic.
Topic:
This is an ebook on software testing. Specifically, website performance testing.
About Veltrano:
Veltrano Solutions is an outsourcing development and software testing firm, and we provide expert services for application development, testing and data analytics. We extend our clients’ software testing capabilities with on-demand technical expertise. Our quality assurance resources work as part of our clients’ teams to help test applications on time and within budget.
Our model is designed to allocate the right mix of local and offshore resources in order to optimize expertise, speed and cost. We provide the ability to quickly add specialty skills to our client’s development team without them incurring long-term costs. The result is far better management of resource capacities and outcomes.
Background on our branding and previous pieces:
I have included a few of our previous ebooks and whitepapers. I like the look and feel of these pieces, however we have made updates to our brand guidelines since them, so the new brand guidelines will need to be incorporated, and I'd like to refresh/update what we have done in the past.
Refer to our website for an idea of our look and feel. This page is one of our newer sections and would be a good reference:
http://www.veltranosol.example/data-analytics/
Tone and feel:
- The look and feel should be professional, clean and polished.
- I like good use of whitespace.
- I would prefer to keep stock photography of people to a minimum. Any images should add to the content and be relevant to the content.
(Also, I uploaded some InDesign files in case you wanted to refer to those assets, but I didn't include the Links folder because they were too big. If there's anything you more you need, let me know)
Target Market(s)
Audience:
The audience is senior Quality Assurance and Software Testing professionals.
- 30-45 years old
- Technical mindset
- Interested in learning
Titles include
- QA Lead
- QA Manager
- QA Director
- Director or VP of Development
- QA Automation Engineer
Our customers are medium to large sized companies. Many are software companies, but many are also enterprises in all almost all industries.

```html
<!DOCTYPE html>
<html lang="en">
<head>
<meta charset="utf-8">
<title>Website Performance Testing eBook – Page Layouts</title>
<link href="https://fonts.googleapis.com/css2?family=Open+Sans:ital,wght@0,400;0,600;0,700;1,400&display=swap" rel="stylesheet">
<style>
  :root {
    --board: #7b7b7b;
    --paper: #ffffff;
    --salmon: #e2837a;
    --accent: #d9564c;
    --ink: #3a3a3a;
    --body: #5c5c5c;
    --muted: #9a9a9a;
    --tab: #cfcfcf;
    --photo-dark: #5a5a5a;
    --photo-light: #d6d6d6;
  }
  * { box-sizing: border-box; margin: 0; padding: 0; }
  html, body { width: 1200px; height: 1200px; overflow: hidden; }
  body {
    background: var(--board);
    font-family: "Open Sans", Arial, sans-serif;
    position: relative;
  }
  .page {
    position: absolute;
    width: 279px;
    height: 361px;
    background: var(--paper);
    overflow: hidden;
  }
  .page-label {
    position: absolute;
    width: 279px;
    text-align: center;
    color: #f2f2f2;
    font-size: 14px;
  }
  .side-band { position: absolute; left: 0; top: 0; bottom: 0; width: 16px; background: var(--salmon); }
  .running-tab {
    position: absolute; left: 16px; top: 5px; height: 6px; width: 92px;
    background: var(--tab); color: #fff; font-size: 3.6px; line-height: 6px; padding-left: 4px;
    clip-path: polygon(0 0, 92% 0, 100% 100%, 0 100%);
  }
  .page:not(.banded) .running-tab { left: 17px; }
  .running-head {
    position: absolute; left: 0; right: 0; top: 10.5px; height: 1px; background: #ececec;
  }
  .brand-mini {
    position: absolute; right: 12px; top: 18px; color: var(--accent);
    font-size: 8px; font-weight: 600; letter-spacing: .1px;
  }
  .content { position: absolute; left: 30px; right: 24px; top: 40px; }
  .banded .content { left: 36px; }
  .title {
    color: var(--accent); font-weight: 700; font-size: 11.5px; line-height: 1.2;
    border-left: 1.5px solid var(--accent); padding-left: 5px; margin-bottom: 9px;
  }
  .title .soft { color: #e9a39c; }
  .subhead { color: var(--ink); font-weight: 700; font-size: 6.4px; margin: 6px 0 5px; }
  .tool { color: var(--accent); font-weight: 600; font-size: 6.6px; margin: 9px 0 4px; }
  p { color: var(--body); font-size: 3.7px; line-height: 1.55; text-align: justify; margin-bottom: 5px; }
  ul { list-style: none; margin-bottom: 5px; }
  li { position: relative; color: var(--body); font-size: 3.7px; line-height: 1.5; padding-left: 7px; margin-bottom: 4px; }
  li::before { content: ""; position: absolute; left: 0; top: 1.6px; width: 2.2px; height: 2.2px; border-radius: 50%; background: var(--accent); }
  li b { color: var(--accent); font-weight: 600; }
  .divider { border-top: .6px dashed #d4d4d4; margin: 20px 24px 22px; }
  .folio {
    position: absolute; bottom: 16px; left: 50%; transform: translateX(-50%);
    width: 6px; height: 6px; border: .6px solid var(--salmon); border-radius: 50%;
    color: var(--salmon); font-size: 3.4px; line-height: 5px; text-align: center;
  }
  .folio::before, .folio::after { content: ""; position: absolute; top: 2.4px; width: 120px; height: .5px; background: #ececec; }
  .folio::before { right: 7px; } .folio::after { left: 7px; }
  .photo { position: absolute; background: linear-gradient(160deg, var(--photo-light), var(--photo-dark)); }

  /* cover */
  .cover-photo { left: 0; top: 0; width: 279px; height: 270px; background: linear-gradient(150deg, #3e3e3e 0%, #8d8d8d 45%, #e4e4e4 100%); }
  .cover-band { position: absolute; left: 0; top: 176px; }
  .cover-title {
    position: absolute; left: 24px; top: 182px; color: #fff; font-weight: 700;
    font-size: 21px; line-height: 1.12; border-left: 1.5px solid #fff; padding-left: 4px;
  }
  .cover-intro { position: absolute; left: 16px; top: 282px; width: 200px; font-size: 3.7px; font-style: italic; color: var(--ink); line-height: 1.5; }
  .cover-brand { position: absolute; right: 16px; top: 308px; text-align: right; }
  .cover-brand .name { color: var(--accent); font-size: 27px; line-height: 1; }
  .cover-brand .sub { color: var(--muted); font-size: 13px; line-height: 1; margin-top: -1px; }
  .cover-kind { position: absolute; left: 16px; bottom: 15px; font-size: 6.4px; color: var(--muted); }

  .twin { display: flex; gap: 14px; }
  .twin > div { flex: 1; text-align: center; }
  .twin .tool { margin-top: 2px; }
  .icon { display: block; margin: 0 auto 2px; }
</style>
</head>
<body>

<!-- Cover -->
<section class="page" style="left:18px;top:16px">
  <div class="photo cover-photo" role="img" aria-label="Black and white photo of hands typing on a laptop beside a coffee mug and tablet"></div>
  <svg class="cover-band" width="279" height="96" viewBox="0 0 279 96" aria-hidden="true">
    <polygon points="0,0 238,0 184,80 0,80" fill="#e2837a" opacity=".93"/>
    <line x1="184" y1="80" x2="279" y2="80" stroke="#d2c08a" stroke-width=".6"/>
    <line x1="184" y1="80" x2="236" y2="2" stroke="#d2c08a" stroke-width=".6"/>
  </svg>
  <h1 class="cover-title">Website<br>Performance<br>Testing</h1>
  <p class="cover-intro">Every web product needs careful testing before release. Users expect fast pages and smooth use, and patience for slow sites runs short, so checking performance is vital.</p>
  <div class="cover-brand"><div class="name">veltrano</div><div class="sub">solutions</div></div>
  <div class="cover-kind">eBook</div>
</section>
<div class="page-label" style="left:18px;top:384px">cover page</div>

<!-- Page 01 -->
<section class="page" style="left:313px;top:16px">
  <div class="running-head"></div><div class="running-tab">Website Performance Testing</div>
  <div class="brand-mini">veltrano</div>
  <div class="content" style="top:30px">
    <h2 class="title">Website Performance Testing</h2>
    <p>Performance testing checks how efficiently a site responds compared with its targets. It measures overall responsiveness under average loads and should start early and often, so that imbalances in the architecture, resource bottlenecks and unexpected latency are found and corrected before later stages of development.</p>
    <p>The end result of these tests is a baseline of measurements you apply whenever the site changes, to ensure responsiveness and processing efficiency stay stable and improve.</p>
    <p>Let us look at two specific types of website testing: Load Testing and Stress Testing.</p>
  </div>
  <div class="photo" style="left:0;top:136px;width:279px;height:120px" role="img" aria-label="Black and white close-up of a hand on a laptop keyboard"></div>
  <div class="content" style="top:262px">
    <div class="twin">
      <div>
        <svg class="icon" width="11" height="11" viewBox="0 0 12 12" aria-hidden="true"><path d="M2 6a4 4 0 0 1 7-2.6M10 6a4 4 0 0 1-7 2.6" fill="none" stroke="#bbb" stroke-width="1"/><path d="M9 1v2.6H6.4M3 11V8.4h2.6" fill="none" stroke="#bbb" stroke-width="1"/></svg>
        <div class="tool">Load Testing</div>
        <p>Early load tests stabilise behaviour. They simulate thousands or millions of users over long periods and suit measuring endurance and volume capacity. They take one step closer to real conditions and uncover buffer overflows, memory leaks and slow degradation.</p>
      </div>
      <div>
        <svg class="icon" width="11" height="11" viewBox="0 0 12 12" aria-hidden="true"><circle cx="5" cy="5" r="3.4" fill="none" stroke="#bbb" stroke-width="1"/><line x1="7.5" y1="7.5" x2="11" y2="11" stroke="#bbb" stroke-width="1.2"/></svg>
        <div class="tool">Stress Testing</div>
        <p>Stress tests push heavy burden on the site to uncover its breaking points. Equally important, they measure how gracefully the site fails and recovers. Success means the site can fail without losing data or creating security risks, then recover quickly.</p>
      </div>
    </div>
  </div>
  <div class="folio">1</div>
</section>
<div class="page-label" style="left:313px;top:384px">page 01</div>

<!-- Page 02 -->
<section class="page" style="left:609px;top:16px">
  <div class="running-head"></div><div class="running-tab">Website Performance Testing</div>
  <div class="brand-mini">veltrano</div>
  <div class="photo" style="left:158px;top:50px;width:121px;height:270px" role="img" aria-label="Black and white photo of a person working on a laptop next to a tea glass"></div>
  <div class="content" style="top:48px;right:128px;left:30px">
    <h2 class="title" style="margin-bottom:14px">Website<br>Performance<br>Testing Approach</h2>
    <p>When designing your web performance testing, use a logical approach that gradually narrows down on defects in design, development and deployment. Start with a clear set of objectives and measurable criteria, otherwise you may waste effort testing the wrong things.</p>
    <p>Plan to start performance testing as early as possible in your development cycle to harvest the low-hanging fruit, such as major imbalances in the software's implementation. If possible, engage developers in the early stages of testing and keep results visible.</p>
    <p>To quick-start your testing effort, it helps to focus your testing and optimisation efforts on the most-used or high-impact pages based on traffic share, which you can learn using analysis tools or logs.</p>
    <p>Finally, regularly review the following do's and don'ts of website performance testing, especially with regard to cloud-based testing.</p>
  </div>
  <div class="folio">2</div>
</section>
<div class="page-label" style="left:609px;top:384px">page 02</div>

<!-- Page 03 -->
<section class="page banded" style="left:903px;top:16px">
  <div class="side-band"></div>
  <div class="running-head"></div><div class="running-tab">Website Performance Testing</div>
  <div class="brand-mini">veltrano</div>
  <div class="content" style="top:48px;left:36px">
    <h2 class="title" style="margin-bottom:14px">The Do's and Don'ts of Website<br>Performance Testing</h2>
    <p>When it is time to implement the test plan, avoid common strategic and tactical pitfalls:</p>
    <ul style="margin-top:12px">
      <li><b>Do</b> keep your in-house test infrastructure up-to-date even if you use cloud-based testing, as it is your baseline for isolating side-effects.</li>
      <li><b>Do</b> use your live site, if one exists, to guide load and stress testing parameters on the developing site.</li>
      <li><b>Do</b> track both client and server-side traffic during non-peak and peak performance testing.</li>
      <li><b>Do</b> test as many pages and combinations of page traversals as possible.</li>
      <li><b>Do</b> pay attention to which pages or activities consume an inordinate amount of time relative to other areas.</li>
      <li><b>Do</b> distribute generated loads geographically and by network segment.</li>
    </ul>
    <div class="divider"></div>
    <ul>
      <li><b>Don't</b> ignore the dependency between page load times and user volume capacity.</li>
      <li><b>Don't</b> forget to process live web traffic logs to collect statistics on request types and volume.</li>
      <li><b>Don't</b> run your load generation on the same cloud as your website.</li>
      <li><b>Don't</b> assume that cloud testing is always less expensive than in-house infrastructure.</li>
      <li><b>Don't</b> rely on a single cloud vendor as distinct functional traits may affect results.</li>
    </ul>
  </div>
  <div class="folio">3</div>
</section>
<div class="page-label" style="left:903px;top:384px">page 03</div>

<!-- Page 04 -->
<section class="page banded" style="left:148px;top:413px">
  <div class="side-band"></div>
  <div class="running-head"></div><div class="running-tab">Website Performance Testing</div>
  <div class="brand-mini">veltrano</div>
  <div class="content" style="top:36px;left:36px">
    <h2 class="title" style="margin-bottom:14px"><span class="soft">Why Use</span> the Cloud for Website<br>Performance Testing</h2>
    <p>Website performance testing with cloud-based tools and infrastructure offers many of the same advantages as cloud-based enterprise apps, such as cost reduction, faster test deployment and dynamic scaling.</p>
    <ul style="margin-top:10px">
      <li><b>Minimizes</b> capital expense for on-site hardware and infrastructure while reducing ongoing costs for maintenance.</li>
      <li><b>Eliminates</b> long hardware acquisition lead times.</li>
      <li><b>Offers</b> choice in selecting vendor features most important to your website testing.</li>
      <li><b>Provides</b> immediate scalability to meet your performance testing scenarios.</li>
      <li><b>Eliminates</b> disruptions due to equipment failure or power outages.</li>
    </ul>
    <p>Additionally, the cloud provides specific benefits that increase the accuracy and efficiency for performance testing.</p>
    <h2 class="title" style="margin-top:24px;margin-bottom:10px">Cloud Benefits for Website<br>Performance Testing</h2>
    <div class="subhead">Realistic Performance Evaluation</div>
    <p>Cloud-based performance testing supplies more realistic conditions beyond the corporate intranet, including those out of your control, such as unpredictable peak events, network congestion or a variety of device and browser mix.</p>
    <p>For example, you can take advantage of virtual infrastructure over specific regions, which might uncover issues with local network infrastructure, regional user conventions or content delivery that a per-region CDN could solve.</p>
  </div>
  <div class="folio">4</div>
</section>
<div class="page-label" style="left:148px;top:777px">page 04</div>

<!-- Page 05 -->
<section class="page" style="left:461px;top:413px">
  <div class="running-head"></div><div class="running-tab">Website Performance Testing</div>
  <div class="brand-mini">veltrano</div>
  <div class="content" style="top:40px">
    <div class="subhead" style="font-size:6.6px">Instant Swap of Test and Deployment Versions</div>
    <p>Cloud-based testing has process advantages as well. The use of virtual server infrastructure plus state-of-the-art deployment tools enables testing different software versions by swapping instances within seconds.</p>
    <p>For instance, instrumented test versions of your website could be exchanged immediately with the deployed version by redirecting your site address to the test version via saved configurations.</p>
    <h2 class="title" style="margin-top:14px">Website Performance Testing Tools</h2>
    <p>Many seasoned tools for testing websites exist on the market today. From simple page-load tools to advanced script-capable tool suites that test both client and server endpoints, there is something for everyone.</p>
    <p>Successful site testing also requires highly experienced testers who know these tools inside and out, including specific techniques for load and stress tests.</p>
  </div>
  <div class="photo" style="left:0;top:195px;width:279px;height:80px" role="img" aria-label="Black and white photo of a hand writing notes beside a keyboard"></div>
  <div class="content" style="top:284px">
    <div class="tool">CrimsonBot</div>
    <p>CrimsonBot is one example of a class of online test tools that measure load times, find bottlenecks or suggest optimisations for HTTP traffic generated by your site. It is useful for initial website analysis and quick spot-check sanity tests.</p>
  </div>
  <div class="folio">5</div>
</section>
<div class="page-label" style="left:461px;top:777px">page 05</div>

<!-- Page 06 -->
<section class="page banded" style="left:774px;top:413px">
  <div class="side-band"></div>
  <div class="running-head"></div><div class="running-tab">Website Performance Testing</div>
  <div class="brand-mini">veltrano</div>
  <div class="content" style="top:34px;left:30px">
    <div class="tool">Kestrel Meter</div>
    <p>This open-source downloadable tool is popular for website load and performance tests. It simulates single and multiple servers over many protocols. Other tools, such as FlareMeter, enable running it in the cloud.</p>
    <div class="tool">Brightwave LoadSuite</div>
    <p>This is another desktop tool used for load, stress and scalability testing for websites built on many frameworks. Tests are created quickly without advanced programming skills, in-house or in the cloud.</p>
    <div class="tool">Quartzite Driver</div>
    <p>This free, open-source tool provides native browser testing remotely or locally. Its API may be accessed with many languages, and multiple virtual web servers can be employed for realistic load and stress testing.</p>
    <div class="tool">Hornet</div>
    <p>Hornet is an open-source server-side tool that runs headless, which means user-driven tests can be automated via scripts and distributed over as many machines as desired.</p>
    <div class="tool">Nimbra CloudCheck</div>
    <p>This well-known cloud-based tool supports web-based functional and performance testing, simulating millions of virtual users across multiple geographic regions.</p>
    <div class="tool">SurgeRun</div>
    <p>This cloud-based tool allows you to simulate user behaviours without knowing a scripting language. It scales up to very large user counts with geographic load distribution.</p>
  </div>
  <div class="folio">6</div>
</section>
<div class="page-label" style="left:774px;top:777px">page 06</div>

<!-- Page 07 -->
<section class="page banded" style="left:289px;top:811px">
  <div class="side-band"></div>
  <div class="running-head"></div><div class="running-tab">Website Performance Testing</div>
  <div class="brand-mini">veltrano</div>
  <div class="content" style="top:34px;left:30px">
    <div class="tool">Torrent.example</div>
    <p>Torrent.example enables website performance testing with virtual users over hundreds of servers. It offers real-time monitoring and results presentation, which enables early termination of tests as problems are discovered.</p>
    <div class="tool" style="margin-top:12px">NovaLoad</div>
    <p>NovaLoad simulates realistic user loads while revealing bottlenecks in website performance. Test generation and maintenance is highly automated via a drag-and-drop interface, letting testers create and update scenarios faster.</p>
    <h2 class="title" style="margin-top:36px;margin-bottom:12px">Engaging with a Testing Partner</h2>
    <p>Your company spends a great deal of resources on the design, development and deployment of your web site, app or service. Software testing, however, may not be your forte when it comes to the nuances of performance, load and stress testing.</p>
    <p>You want the most realistic testing scenarios possible, but may not be keen on spinning up all the testing technologies and tools available.</p>
    <p>That is why it often pays to engage with a trusted, experienced QA partner such as <span style="color:var(--accent)">Veltrano Solutions</span>.</p>
    <p>At Veltrano, we provide end-to-end testing services from development to production, including load, stress, spike and configuration testing, working hand-in-hand with you so you can focus on what you do best.</p>
  </div>
  <div class="folio">7</div>
</section>
<div class="page-label" style="left:289px;top:1175px">page 07</div>

<!-- Page 08 -->
<section class="page" style="left:623px;top:811px">
  <div class="running-head"></div><div class="running-tab">Website Performance Testing</div>
  <div class="brand-mini">veltrano</div>
  <div class="photo" style="left:0;top:40px;width:279px;height:155px" role="img" aria-label="Black and white photo of a person reviewing printed charts at a desk with a laptop"></div>
  <div class="content" style="top:205px">
    <h2 class="title">Conclusion</h2>
    <p>It is a well-known truism that if your website fails to respond within a few seconds, half of your visitors leave and may never return. Responsiveness is the gateway to keeping customers engaged.</p>
    <p>Despite the ready availability of testing tools, many factors are involved in delivering world-class responsiveness, requiring high-level performance testing expertise across devices, apps and infrastructure.</p>
    <p>Taking a step-by-step approach that ramps up demand on your site or service is the best strategy, paired with a realistic, geographically dispersed cloud test platform.</p>
    <p>Attention to detail, diligence and understanding the nuances of performance testing will lead you to success.</p>
  </div>
  <div class="folio">8</div>
</section>
<div class="page-label" style="left:623px;top:1175px">page 08</div>

</body>
</html>
```